New Construction company looking for powerful bold logo. people see the logo, leaves an impression

We need a business card for our new company. We provide site work for commercial projects in South Texas. We clear land, excavation, run under ground utilities, concrete work, dirt work etc. We like the black card. I created a webpage www.tarn-vbuilders.com .... As I grow with projects I will put up pictures with video, and intro music. Want it look cool, bold, powerful, and slick looking. Creating 'TVB'....as my logo (possibly or if you have something you want to have fun with). Just have fun!!....thank you!

Dorian Pruett Business Manager Serving South Texas PO Box 4837 Carrow,TX. 78395 Mobile: 361-752-6083 www.tarn-vbuilders.com dorian@tarn-vbuilders.com you can put this anyway you see fit in your design and layout. thank you

Target Market(s)

General Contractors; Home Builders;

Industry/Entity Type

Construction

Contact Information for Business Card

I want the card to be black.

Font styles to use
Other font styles liked:
• Designer choice

Requirements
Must have
• Tarn-V Construction
• Site Work - Utilities/Concrete/Pad/Grading/Excavation (on the back side)
Nice to have
• Maybe TVB as the logo.....or just a symbol that would be TV.....and then construction to tie it togther...

```html
<!DOCTYPE html>
<html lang="en">
<head>
<meta charset="utf-8">
<title>Tarn-V Construction – Business Card</title>
<link rel="stylesheet" href="https://fonts.googleapis.com/css2?family=Alegreya:wght@400&family=Lato:wght@400;700&display=swap">
<style>
  :root {
    --page-bg: #f0f0f0;
    --card-black: #121212;
    --band-dark: #1c1c1c;
    --texture-mid: #2d2d2d;
    --texture-edge: #242424;
    --gold: #dcbc3f;
    --text-light: #f2f2f2;
    --text-soft: #d6d6d6;
  }
  * { margin: 0; padding: 0; box-sizing: border-box; }
  html, body {
    width: 1052px; height: 1200px; overflow: hidden;
    background: var(--page-bg);
  }
  .card {
    position: absolute; left: 38px; width: 975px; height: 556px;
    background: var(--card-black); overflow: hidden;
  }
  .card--front { top: 28px; }
  .card--back { top: 609px; }
  .card__bands { position: absolute; inset: 0; width: 975px; height: 556px; }

  .accent-tab { position: absolute; left: 0; top: 180px; width: 36px; height: 196px; }

  .person { position: absolute; left: 66px; top: 232px; color: var(--text-light); }
  .person__name {
    font-family: "Alegreya", Georgia, serif; font-weight: 400;
    font-size: 52px; line-height: 1; letter-spacing: 0.5px;
  }
  .person__title {
    font-family: "Lato", Arial, sans-serif; font-size: 21px;
    margin-top: 6px; color: var(--text-soft);
  }

  .brand-mark {
    position: absolute; left: 431px; width: 112px;
    display: flex; align-items: center; justify-content: center;
    font-family: "Lato", Arial, sans-serif; font-weight: 700;
    font-size: 40px; letter-spacing: 2px; color: var(--gold);
  }
  .card--front .brand-mark { top: 252px; height: 50px; }
  .card--back .brand-mark { top: 196px; height: 50px; }

  .contact { position: absolute; left: 596px; top: 196px; list-style: none; }
  .contact__item {
    display: flex; align-items: center; height: 36px;
    font-family: "Lato", Arial, sans-serif; font-size: 22px; color: var(--text-soft);
  }
  .contact__item--address { height: auto; align-items: flex-start; line-height: 35px; margin-bottom: 4px; }
  .contact__icon { width: 18px; height: 20px; margin-right: 12px; flex: none; }
  .contact__item--address .contact__icon { margin-top: 6px; }

  .services {
    position: absolute; left: 0; right: 0; top: 492px; text-align: center;
    font-family: "Lato", Arial, sans-serif; font-size: 22px; color: var(--text-light);
  }
</style>
</head>
<body>

<section class="card card--front" aria-label="Business card front">
  <svg class="card__bands" viewBox="0 0 975 556" aria-hidden="true">
    <defs>
      <linearGradient id="texture-front" x1="0" y1="0" x2="0" y2="1">
        <stop offset="0" stop-color="var(--texture-edge)"/>
        <stop offset="0.5" stop-color="var(--texture-mid)"/>
        <stop offset="1" stop-color="var(--texture-edge)"/>
      </linearGradient>
    </defs>
    <rect x="0" y="0" width="975" height="556" fill="var(--band-dark)"/>
    <polygon points="0,88 430,88 487,145 544,88 975,88 975,469 544,469 487,412 430,469 0,469"
             fill="url(#texture-front)"/>
  </svg>

  <svg class="accent-tab" viewBox="0 0 36 196" aria-hidden="true">
    <polygon points="0,0 36,98 0,196" fill="var(--gold)"/>
  </svg>

  <div class="person">
    <h1 class="person__name">Dorian Pruett</h1>
    <p class="person__title">Business Manager</p>
  </div>

  <div class="brand-mark">TVB</div>

  <ul class="contact">
    <li class="contact__item contact__item--address">
      <svg class="contact__icon" viewBox="0 0 18 20" aria-hidden="true">
        <path d="M9 0a7 7 0 0 0-7 7c0 5 7 13 7 13s7-8 7-13a7 7 0 0 0-7-7zm0 10a3 3 0 1 1 0-6 3 3 0 0 1 0 6z" fill="var(--gold)"/>
      </svg>
      <span>South Texas PO Box 4837<br>Carrow,TX. 78395</span>
    </li>
    <li class="contact__item">
      <svg class="contact__icon" viewBox="0 0 18 20" aria-hidden="true">
        <path d="M4 3l3 0 1.5 4-2 1.5a10 10 0 0 0 5 5l1.5-2 4 1.5v3a2 2 0 0 1-2 2A14 14 0 0 1 2 5a2 2 0 0 1 2-2z" fill="var(--gold)"/>
      </svg>
      <span>361-752-6083</span>
    </li>
    <li class="contact__item">
      <svg class="contact__icon" viewBox="0 0 18 20" aria-hidden="true">
        <rect x="1" y="5" width="16" height="11" fill="var(--gold)"/>
        <path d="M1 5l8 6 8-6" fill="none" stroke="var(--band-dark)" stroke-width="1.5"/>
      </svg>
      <span>dorian@tarn-vbuilders.com</span>
    </li>
    <li class="contact__item">
      <svg class="contact__icon" viewBox="0 0 18 20" aria-hidden="true">
        <g fill="none" stroke="var(--gold)" stroke-width="1.4">
          <circle cx="9" cy="10" r="7"/>
          <ellipse cx="9" cy="10" rx="3" ry="7"/>
          <path d="M2 10h14M3.5 6h11M3.5 14h11"/>
        </g>
      </svg>
      <span>www.tarn-vbuilders.com</span>
    </li>
  </ul>
</section>

<section class="card card--back" aria-label="Business card back">
  <svg class="card__bands" viewBox="0 0 975 556" aria-hidden="true">
    <defs>
      <linearGradient id="texture-back" x1="0" y1="0" x2="0" y2="1">
        <stop offset="0" stop-color="var(--texture-mid)"/>
        <stop offset="1" stop-color="var(--texture-edge)"/>
      </linearGradient>
    </defs>
    <rect x="0" y="0" width="975" height="556" fill="var(--band-dark)"/>
    <polygon points="0,0 975,0 975,409 548,409 489,468 430,409 0,409" fill="url(#texture-back)"/>
  </svg>

  <div class="brand-mark">TVB</div>

  <p class="services">Utilities, Concrete, Pad, Grading, Excavation</p>
</section>

</body>
</html>
```